Business Cards

Business cards (double-sided) to be handed out to clients and potential clients, with contact details, logo .

Target Market(s)

Small to medium size businesses

Industry/Entity Type

Accountants

Contact Information for Business Card

Brightwater Ledger & Counsel Ltd

Colors

Designer to choose only greyscale colors for use in the design.

Requirements
Must have
• Name, Title, Address, Phone number, Email, Website
Nice to have
• Modern, clean lines, classy
Should not have
• Business cards to be double-sided. Form keeps reverting to single-sided.

```html
<!DOCTYPE html>
<html lang="en">
<head>
<meta charset="utf-8">
<title>Brightwater Ledger &amp; Counsel – Business Cards</title>
<link href="https://fonts.googleapis.com/css2?family=Jost:wght@300;400&display=swap" rel="stylesheet">
<style>
  :root {
    --backdrop: #3b3b3b;
    --card: #050505;
    --ink: #e6e6e6;
    --ink-soft: #cfcfcf;
    --rule: #bdbdbd;
  }
  * { margin: 0; padding: 0; box-sizing: border-box; }
  html, body { width: 1200px; height: 689px; overflow: hidden; }
  body {
    background: var(--backdrop);
    font-family: "Jost", "Futura", sans-serif;
    color: var(--ink);
  }
  .canvas {
    position: relative;
    width: 1200px;
    height: 689px;
  }
  .card {
    position: absolute;
    top: 190px;
    width: 540px;
    height: 309px;
    background: var(--card);
    box-shadow: 0 18px 40px rgba(0,0,0,0.45);
  }
  .card--front { left: 40px; }
  .card--back { left: 620px; }

  /* Front */
  .wordmark {
    position: absolute;
    inset: 0;
    display: flex;
    align-items: center;
    justify-content: center;
    gap: 16px;
  }
  .wordmark__square {
    width: 14px;
    height: 14px;
    background: var(--ink);
  }
  .wordmark__name {
    font-weight: 400;
    font-size: 26px;
    letter-spacing: 4px;
    line-height: 1.3;
    text-transform: uppercase;
    color: var(--ink);
  }

  /* Back */
  .identity {
    position: absolute;
    right: 290px;
    top: 104px;
    text-align: right;
  }
  .identity__name {
    font-weight: 400;
    font-size: 28px;
    letter-spacing: 0.5px;
    line-height: 1;
  }
  .identity__title {
    font-weight: 300;
    font-size: 12.5px;
    color: var(--ink-soft);
    margin-top: 4px;
  }
  .divider {
    position: absolute;
    left: 268px;
    top: 78px;
    width: 1px;
    height: 110px;
    background: var(--rule);
  }
  .contacts {
    position: absolute;
    left: 288px;
    top: 76px;
    list-style: none;
    font-weight: 300;
    font-size: 12px;
    line-height: 1.35;
    color: var(--ink-soft);
  }
  .contacts__item {
    display: flex;
    align-items: flex-start;
    gap: 8px;
  }
  .contacts__item--address { margin-bottom: 6px; }
  .contacts__icon {
    width: 9px;
    height: 9px;
    margin-top: 3px;
    flex: none;
    fill: var(--ink-soft);
  }
  .company-line {
    position: absolute;
    left: 0;
    right: 0;
    bottom: 46px;
    text-align: center;
    padding-left: 110px;
    font-weight: 300;
    font-size: 14px;
    color: var(--ink-soft);
  }
</style>
</head>
<body>
<main class="canvas">

  <section class="card card--front" aria-label="Card front">
    <div class="wordmark">
      <span class="wordmark__square" aria-hidden="true"></span>
      <span class="wordmark__name">Brightwater<br>Ledger &amp; Counsel</span>
    </div>
  </section>

  <section class="card card--back" aria-label="Card back">
    <div class="identity">
      <p class="identity__name">DANIEL REYES</p>
      <p class="identity__title">Founder &amp; CEO</p>
    </div>

    <span class="divider" aria-hidden="true"></span>

    <ul class="contacts">
      <li class="contacts__item contacts__item--address">
        <svg class="contacts__icon" viewBox="0 0 10 10" aria-hidden="true"><path d="M5 0a3.5 3.5 0 0 0-3.5 3.5C1.5 6 5 10 5 10s3.5-4 3.5-6.5A3.5 3.5 0 0 0 5 0zm0 5a1.4 1.4 0 1 1 0-2.8A1.4 1.4 0 0 1 5 5z"/></svg>
        <span>Street address, City<br>State &amp; ZIP code Country</span>
      </li>
      <li class="contacts__item">
        <svg class="contacts__icon" viewBox="0 0 10 10" aria-hidden="true"><path d="M2 0.5l1.6 2.2-0.9 1.1c0.6 1.2 1.4 2 2.6 2.6l1.1-0.9 2.2 1.6-0.9 1.9C4 8.6 1.4 6 0.5 1.8z"/></svg>
        <span>555-018-2047</span>
      </li>
      <li class="contacts__item">
        <svg class="contacts__icon" viewBox="0 0 10 10" aria-hidden="true"><path d="M0 2h10v6H0z M0.6 2.4L5 5.6l4.4-3.2" fill="none" stroke="currentColor"/><path d="M0 2h10L5 5.5z"/><rect x="0" y="2" width="10" height="6" fill="none" stroke="#cfcfcf" stroke-width="1"/></svg>
        <span>daniel@BrightwaterLedger.com</span>
      </li>
      <li class="contacts__item">
        <svg class="contacts__icon" viewBox="0 0 10 10" aria-hidden="true"><circle cx="5" cy="5" r="4.5" fill="none" stroke="#cfcfcf"/><path d="M0.5 5h9M5 0.5c-2 2.5-2 6.5 0 9M5 0.5c2 2.5 2 6.5 0 9" fill="none" stroke="#cfcfcf" stroke-width="0.8"/></svg>
        <span>BrightwaterLedger.com</span>
      </li>
    </ul>

    <p class="company-line">Brightwater Ledger &amp; Counsel Ltd</p>
  </section>

</main>
</body>
</html>
```